Restaurant Poster Design Project for A-Frame

I am after a poster, which will go on an outdoor A-Frame (A1 size - this size is to be confirmed) outlining our drink/happy hour/specials for our Mexican Restaurant and Bar.

Specific details are:

$4 Beer, Wine and Spirits
$5 Margaritas
everynight 5:30pm-7:30pm

I will supply logo, which needs to be incorporated (really small) into the poster, along with our address: 42 Lowden Road, Windsor - (Im not too sure if we should include our phone number or not ?? Please advise what you feel will look good etc

Happy for you to add a phrase or wording etc, as long as the specific details are included, above.

We also have an enclosed beer garden in the rear of the restaurant - Do you believe I should mention this?

I am really open to eye catching designs and ALL suggestions welcome please!
Updates

Please find attached of samples that I am sort of after: (please let me know if they cant be opened).

http://www.flyerquill.example/blog/wp-content/uploads/2012/06/happyHourPoster-e1340372894746.gif

http://marekvu.files.samplepress.example/2012/10/profolio_0012.jpg?w=1169

http://3.img.noteleaf.example/-NfNjpdG5w/T5pohPd0AhI/AAAAAAAADRs/CA7DPeI_PyU/s640/vintage_poster.jpg

http://www.orchidvane.example/files/imagecache/Event/news/teaser/Lounge_Happy_Hour_Poster_-_Mar_2011_bilingual.jpg

http://www.tkrumps.example/dallas/images/happyhour_poster.jpg

http://cdn2-b.newsgrove.example/sites/default/files/styles/large_lightbox/hash/9a/d1/9ad11350ba178511886fddcff7aaac8d.jpg?itok=wDl2vlfJ

http://www.platterpicks.example/imageservice/images/13/1313171414293_244/img_large_watermarked.jpg

Target Market(s)

18 YEARS OLD AND OVER

Industry/Entity Type

Restaurant

Requirements
Must have
• Address
Phone Number
Logo
Clear easy to read font, to be seen via cars + ppl walking down street
If images are included, to be clear and visable
Nice to have
• Images are possible
To mention a beer garden
Should not have
• Traditional Mexican Colourful 80's Theme

```html
<!DOCTYPE html>
<html lang="en">
<head>
<meta charset="utf-8">
<title>Happy Hour – Casa Lomita</title>
<link rel="stylesheet" href="https://fonts.googleapis.com/css2?family=Bebas+Neue&family=Josefin+Sans:wght@700&display=swap">
<style>
  :root {
    --ink: #000000;
    --paper: #ffffff;
    --rule: #e6e6e6;
    --red: #c8261c;
    --orange: #d9731c;
    --green: #3f8a2a;
    --social: #3b5a9a;
  }
  * { margin: 0; padding: 0; box-sizing: border-box; }
  html, body { width: 848px; height: 1200px; overflow: hidden; background: var(--ink); }
  .poster {
    position: relative;
    width: 848px;
    height: 1200px;
    background: var(--ink);
    color: var(--paper);
    font-family: "Bebas Neue", "Arial Narrow", sans-serif;
  }
  .headline { position: absolute; left: 0; top: 0; width: 848px; height: 400px; }
  .headline text {
    font-family: "Josefin Sans", "Century Gothic", sans-serif;
    font-weight: 700;
  }
  .rule { position: absolute; left: 0; width: 848px; height: 6px; background: var(--rule); }
  .rule--top { top: 402px; }
  .rule--bottom { top: 729px; }

  .drinks-band {
    position: absolute; left: 0; top: 411px; width: 848px; height: 315px;
    display: flex;
  }
  .drinks-edge, .drinks-panel { height: 100%; }
  .drinks-edge--left {
    width: 97px;
    background: linear-gradient(90deg, #2a0806, #7a1a10 70%, #a8281a);
  }
  .drinks-edge--right {
    width: 83px;
    background: linear-gradient(90deg, #6a3a12, #3a200c 60%, #1e1008);
  }
  .drinks-panel { width: 224px; }
  .drinks-panel--red {
    background:
      radial-gradient(ellipse 38% 40% at 50% 34%, #f6dcd8 0%, #eaa69c 45%, rgba(200,38,28,0) 100%),
      linear-gradient(180deg, #7a1c12 0%, var(--red) 55%, #a8241a 100%);
  }
  .drinks-panel--orange {
    background:
      radial-gradient(ellipse 38% 40% at 50% 34%, #fae6da 0%, #efb288 45%, rgba(217,115,28,0) 100%),
      linear-gradient(180deg, #7a3612 0%, #c45a1c 55%, #a6481a 100%);
  }
  .drinks-panel--green {
    background:
      radial-gradient(ellipse 38% 40% at 50% 34%, #f6f2de 0%, #d8d49a 45%, rgba(63,138,42,0) 100%),
      linear-gradient(180deg, #4a4a16 0%, #6a7a24 55%, var(--green) 100%);
  }

  .offer { position: absolute; left: 0; top: 740px; width: 848px; height: 330px; }
  .offer text { font-family: "Bebas Neue", "Arial Narrow", sans-serif; fill: var(--paper); }

  .brand {
    position: absolute; left: 55px; top: 1084px; width: 215px;
    display: flex; align-items: center; gap: 10px;
    font-size: 40px; color: var(--paper); white-space: nowrap;
  }
  .brand-dot { width: 22px; height: 22px; border-radius: 50%; background: var(--red); flex: none; }
  .address {
    position: absolute; left: 300px; top: 1064px; width: 160px;
    font-style: normal; text-align: center; font-size: 28px; line-height: 30px;
  }
  .social-square { position: absolute; left: 527px; top: 1066px; width: 62px; height: 60px; background: var(--social); border-radius: 4px; }
  .social-handle { position: absolute; left: 597px; top: 1083px; font-size: 26px; white-space: nowrap; }
  .website { position: absolute; left: 529px; top: 1130px; font-size: 26px; white-space: nowrap; }
</style>
</head>
<body>
<main class="poster">
  <svg class="headline" viewBox="0 0 848 400" role="img" aria-label="Happy Hour, letters filled with a red, white and green drinks photograph">
    <defs>
      <linearGradient id="headline-fill" x1="0" y1="0" x2="1" y2="0">
        <stop offset="0" stop-color="#f4dedb"/>
        <stop offset="0.3" stop-color="#c8261c"/>
        <stop offset="0.5" stop-color="#f3e7e0"/>
        <stop offset="0.75" stop-color="#b23a22"/>
        <stop offset="1" stop-color="#3f8a2a"/>
      </linearGradient>
    </defs>
    <text x="55" y="194" font-size="190" textLength="738" lengthAdjust="spacingAndGlyphs" fill="url(#headline-fill)">HAPPY</text>
    <text x="133" y="376" font-size="190" textLength="576" lengthAdjust="spacingAndGlyphs" fill="url(#headline-fill)">HOUR</text>
  </svg>

  <div class="rule rule--top"></div>
  <div class="drinks-band">
    <div class="drinks-edge drinks-edge--left" role="img" aria-label="Dark red blurred bar interior"></div>
    <div class="drinks-panel drinks-panel--red" role="img" aria-label="Salt-rimmed frozen margarita with lime wedges, tinted red"></div>
    <div class="drinks-panel drinks-panel--orange" role="img" aria-label="Salt-rimmed frozen margarita with lemon wedges, tinted orange"></div>
    <div class="drinks-panel drinks-panel--green" role="img" aria-label="Salt-rimmed frozen margarita with lime wedges, tinted green"></div>
    <div class="drinks-edge drinks-edge--right" role="img" aria-label="Dark brown blurred bar interior"></div>
  </div>
  <div class="rule rule--bottom"></div>

  <svg class="offer" viewBox="0 740 848 330">
    <text x="203" y="800" font-size="60" textLength="602" lengthAdjust="spacingAndGlyphs">ENJOY A GOOD TIME IN OUR BEER GARDEN</text>
    <text x="260" y="849" font-size="52" textLength="334" lengthAdjust="spacingAndGlyphs">WITH THIS SPECIAL</text>
    <text x="184" y="915" font-size="74" textLength="627" lengthAdjust="spacingAndGlyphs">BEER, WINE AND SPIRITS - ONLY $4</text>
    <text x="184" y="987" font-size="74" textLength="506" lengthAdjust="spacingAndGlyphs">MARGARITAS - ONLY $5</text>
    <text x="242" y="1051" font-size="39" textLength="385" lengthAdjust="spacingAndGlyphs">EVERY NIGHT 5:30PM-7:30PM</text>
  </svg>

  <div class="brand"><span class="brand-dot"></span><span>Casa Lomita</span></div>

  <address class="address">42 LOWDEN RD<br>WINDSOR<br>03 9555 0142</address>

  <div class="social-square"></div>
  <span class="social-handle">/CASALOMITARESTAURANTS</span>
  <p class="website">HTTP://WWW.CASALOMITA.EXAMPLE</p>
</main>
</body>
</html>
```